"Brightly Bold Sisters" book

I am self-publishing a legal guide for women, which will give them information about their rights and how to navigate the legal world in an easy-to-read style. I'd like to see a design using the colours in the logo I've also had designed for the brand by the same name. Then I can provide the winner my photo and a blurb for the back cover. I am the author: Melda Strovik.

Font styles to use
Serif

Requirements
Must have
• Casual but trustworthy feel. Not too formal - it's not a legal text book.
• Back cover must have my photo, a space for the blurb, and a space for the barcode
Nice to have
• Abstract - not my photo on the front, and not a bunch of smiling women either.

```html
<!DOCTYPE html>
<html lang="en">
<head>
<meta charset="utf-8">
<title>Brightly Bold Sisters — Melda Strovik</title>
<link rel="stylesheet" href="https://fonts.googleapis.com/css2?family=Cinzel:wght@400&family=Sacramento&display=swap">
<style>
  :root {
    --paper: #ffffff;
    --taupe: #73685b;
    --gold: #c3962f;
    --honey: #eeb354;
    --caramel: #b3844f;
  }
  html, body {
    margin: 0;
    padding: 0;
    overflow: hidden;
    background: var(--paper);
  }
  .book-cover {
    position: relative;
    width: 800px;
    height: 1200px;
    background: var(--paper);
    overflow: hidden;
  }
  .cover-title {
    position: absolute;
    left: 0;
    top: 0;
    width: 800px;
    height: 480px;
  }
  .cover-title text {
    font-family: "Sacramento", cursive;
  }
  .title-line--first { fill: var(--taupe); }
  .title-word--accent { fill: var(--gold); }
  .title-word--main { fill: var(--taupe); }

  .brand-mark {
    position: absolute;
    left: 150px;
    top: 560px;
    width: 520px;
    height: 420px;
    display: flex;
    align-items: center;
    justify-content: center;
    gap: 36px;
  }
  .brand-mark__dot {
    flex: 0 0 auto;
    width: 170px;
    height: 170px;
    border-radius: 50%;
    background: var(--honey);
  }
  .brand-mark__name {
    font-family: "Cinzel", serif;
    font-weight: 400;
    font-size: 54px;
    line-height: 1.25;
    letter-spacing: 3px;
    color: var(--caramel);
  }

  .author-name {
    position: absolute;
    left: 0;
    top: 1108px;
    width: 800px;
    margin: 0;
    text-align: center;
    font-family: "Cinzel", serif;
    font-weight: 400;
    font-size: 42px;
    line-height: 56px;
    letter-spacing: 9px;
    color: var(--taupe);
  }
</style>
</head>
<body>
  <main class="book-cover">
    <svg class="cover-title" viewBox="0 0 800 480" aria-label="Brightly Bold Sisters" role="heading" aria-level="1">
      <text class="title-line--first" x="180" y="230" font-size="210" textLength="440" lengthAdjust="spacingAndGlyphs">Brightly</text>
      <text x="48" y="430" font-size="190" textLength="704" lengthAdjust="spacingAndGlyphs"><tspan class="title-word--accent">Bold</tspan><tspan class="title-word--main">Sisters</tspan></text>
    </svg>

    <div class="brand-mark">
      <span class="brand-mark__dot"></span>
      <span class="brand-mark__name">Brightly<br>Bold<br>Sisters</span>
    </div>

    <p class="author-name">MELDA STROVIK</p>
  </main>
</body>
</html>
```